EPC Marketing Flyer TH Tidewell

Company Name: Tidewell Housing Ltd
Product: Residential EPCs
Territory: Nationwide (UK)
Marketing channel: Flyer will be used for email and postal mailshots. We have not targeted this particular segment of the market before, so we need it to be eye catching, clearly messaged and encourage the recipient to get in touch.

We need a flyer to promote our services to conduct EPCs owned by public and private sector for residential ONLY (NOT Commercial), on a large or small scale.

Our Surveyors: experienced and accredited surveyors, quality service, quick and professional

Our Business: Warm Path Accredited, Reputation in business for excellence, fast growing

Our Service: Friendly, high quality, quick and professional

Colours: Designs in green and white (same shade as corporate colours), with our logo, and warm path accreditation logo, promoting our business.

Target Market(s)

Estate Agencies, Housing Associations, Local Authorities (Housing Departments), House Builders (NOT Home Owners Directly)

Industry/Entity Type

It Company

Font styles to use
Sans Serif
Other font styles liked:
• Calibri

Colors
add136
9bcb3c
cadf82
f6faec
eaf2ce

Requirements
Must have
• Our contact number etc must be clearly visible, and that we do EPCs
• Must state: What is an EPC? An EPC (Energy Performance Certificate) gives a property an energy efficiency rating from A (most efficient) to G (least efficient) and is valid for 10 years. An EPC can also provide recommendations on home improvement measures which once complete can improve the energy efficiency of the property.
• Who needs and EPC? All landlords and home owners, as all properties available to buy or rent require a valid and current EPC.
• Contact details:
• Tel: 08000 614 905
• Website: www.th-tidewell.co.uk
• Email: epc@th-tidewell.co.uk
• we must also be ably to print out the flyer
Nice to have
• Nice images to accompany the text which give a feeling of Environmentally Green, Home Energy Efficiency, Home Warmth and family - see example attached. And image of survey professional at work.
Should not have
• Any reference to cost or pricing
• Warm path logo art work must not be any other size that that specified in guidance document attached.

```html
<!DOCTYPE html>
<html lang="en">
<head>
<meta charset="utf-8">
<title>Residential EPCs – Tidewell Housing Ltd</title>
<link href="https://fonts.googleapis.com/css2?family=Open+Sans:wght@400;600;700&family=Roboto+Condensed:wght@700&display=swap" rel="stylesheet">
<style>
  :root {
    --green: #8cc63f;
    --green-light: #add136;
    --green-pale: #eaf2ce;
    --green-wash: #f6faec;
    --green-dark: #3d8b2f;
    --green-heading: #4a8a2e;
    --charcoal: #2f2f2f;
    --text: #3a3a3a;
    --white: #ffffff;
    --page: #e9ebe6;
  }
  * { margin: 0; padding: 0; box-sizing: border-box; }
  html, body { width: 900px; height: 1200px; overflow: hidden; background: var(--page); }
  body { font-family: "Open Sans", Arial, sans-serif; color: var(--text); }

  .flyer {
    position: absolute; left: 20px; top: 10px; width: 860px; height: 1180px;
    background: linear-gradient(180deg, var(--white) 40%, var(--green-wash) 60%, var(--white) 70%);
    overflow: hidden;
    box-shadow: 0 4px 14px rgba(0,0,0,.25);
  }
  .hero-photo {
    position: absolute; left: 0; top: 0; width: 860px; height: 350px;
    background: linear-gradient(180deg, #3f7fc4 0%, #8dbbe6 45%, #cfe3f3 70%, #9ccc55 88%, #6fa532 100%);
  }
  .swoosh { position: absolute; left: 0; width: 860px; }
  .swoosh-top { top: 250px; height: 140px; }
  .swoosh-bottom { top: 700px; height: 480px; }

  .hero-title {
    position: absolute; right: 40px; top: 22px; text-align: right;
  }
  .hero-title h1 {
    font-family: "Roboto Condensed", Arial, sans-serif; font-weight: 700;
    font-size: 40px; color: #3b4147; line-height: 1;
  }
  .hero-title p { font-size: 16px; font-weight: 700; color: #1c1c1c; margin-top: 10px; }

  .brand {
    position: absolute; left: 45px; top: 360px; display: flex; align-items: center; gap: 14px;
  }
  .brand-dot { width: 70px; height: 70px; border-radius: 50%; background: var(--green); }
  .brand-name { font-size: 30px; font-weight: 400; color: var(--green-heading); line-height: 1.1; }

  .website {
    position: absolute; left: 447px; top: 398px;
    font-size: 23px; font-weight: 700; color: #3b4147;
  }

  .divider {
    position: absolute; left: 425px; top: 510px; width: 1px; height: 230px; background: #bfbfbf;
  }

  .section-heading {
    font-family: "Roboto Condensed", Arial, sans-serif; font-weight: 700;
    color: var(--green-heading); font-size: 29px; line-height: 1.1;
  }
  .epc-intro { position: absolute; left: 41px; top: 502px; width: 362px; }
  .epc-intro p {
    margin-top: 14px; font-size: 14.5px; line-height: 1.45; text-align: justify; color: var(--text);
  }

  .about { position: absolute; left: 447px; top: 502px; width: 390px; }
  .about-item { font-size: 20px; line-height: 1.3; font-weight: 600; color: #333; margin-bottom: 22px; }
  .about-item strong { color: var(--green-heading); font-weight: 700; }
  .about .section-heading { font-size: 27px; margin-top: 2px; }
  .about p.small { font-size: 14.5px; line-height: 1.45; margin-top: 10px; }

  .badge {
    position: absolute; left: 262px; top: 736px; width: 158px; height: 158px; border-radius: 50%;
    background: #d9d9d9; border: 4px solid var(--white); box-shadow: 0 0 0 2px #555;
  }

  .services { position: absolute; left: 41px; top: 838px; }
  .services h2 {
    font-family: "Roboto Condensed", Arial, sans-serif; font-weight: 700;
    color: var(--white); font-size: 29px; line-height: 1.05;
    text-shadow: 0 1px 2px rgba(0,0,0,.25);
  }
  .services ul { list-style: none; margin-top: 18px; }
  .services li {
    font-size: 20px; font-weight: 700; color: #1c1c1c; line-height: 29px;
    display: flex; align-items: center; gap: 14px;
  }
  .services li::before {
    content: ""; width: 15px; height: 15px; border-radius: 50%;
    background: var(--white); border: 4px solid #555; flex: none;
  }

  .contact { position: absolute; left: 41px; top: 1080px; }
  .contact .phone {
    font-family: "Roboto Condensed", Arial, sans-serif; font-weight: 700;
    font-size: 36px; color: #111;
  }
  .contact .email { font-size: 19px; font-weight: 700; color: #111; margin-top: 4px; }

  .consult {
    position: absolute; left: 548px; top: 884px; width: 250px; height: 176px; border-radius: 50%;
    background: var(--green-dark); border: 5px solid var(--white);
    display: flex; align-items: center; justify-content: center; text-align: center;
    font-family: "Roboto Condensed", Arial, sans-serif; font-weight: 700;
    font-size: 26px; line-height: 1.2; color: var(--white);
  }
  .territory { position: absolute; left: 560px; top: 1068px; width: 250px; text-align: center; }
  .territory h3 {
    font-family: "Roboto Condensed", Arial, sans-serif; font-weight: 700; font-size: 27px; color: #111;
  }
  .territory p { font-size: 14.5px; font-weight: 600; color: #111; line-height: 1.45; margin-top: 4px; }
</style>
</head>
<body>
<main class="flyer">
  <div class="hero-photo" role="img" aria-label="Sky with clouds over grass, a light green house illustration on the left and a smiling family lying on the lawn on the right"></div>

  <svg class="swoosh swoosh-top" viewBox="0 0 860 140" preserveAspectRatio="none" aria-hidden="true">
    <path d="M0 20 C250 110 550 110 860 55 L860 140 L0 140 Z" fill="#ffffff"/>
    <path d="M0 5 C260 105 560 100 860 50 L860 62 C560 110 260 118 0 30 Z" fill="#8cc63f"/>
    <path d="M0 32 C260 118 560 112 860 64 L860 70 C560 118 260 126 0 42 Z" fill="#cadf82"/>
  </svg>

  <header class="hero-title">
    <h1>Residential EPCs</h1>
    <p>Friendly, high quality, quick and professional</p>
  </header>

  <div class="brand">
    <span class="brand-dot"></span>
    <span class="brand-name">Tidewell Housing Ltd</span>
  </div>
  <div class="website">www.th-tidewell.co.uk</div>

  <section class="epc-intro">
    <h2 class="section-heading">What is an EPC?</h2>
    <p>An EPC (Energy Performance Certificate) gives a property an energy efficiency rating from A (most efficient) to G (least efficient) and is valid for 10 years. An EPC can also provide recommendations on home improvement measures which once complete can improve the energy efficiency of the property.</p>
  </section>

  <div class="divider"></div>

  <section class="about">
    <p class="about-item"><strong>Our Surveyors:</strong> Experienced and accredited surveyors, quality service, quick and professional</p>
    <p class="about-item"><strong>Our Business:</strong> Warm Path Accredited, Reputation in business for excellence, fast growing</p>
    <h2 class="section-heading">Who needs and EPC?</h2>
    <p class="small">All landlords and home owners, as all properties available to buy or rent require a valid and current EPC.</p>
  </section>

  <svg class="swoosh swoosh-bottom" viewBox="0 0 860 480" preserveAspectRatio="none" aria-hidden="true">
    <path d="M0 130 C300 180 560 190 860 140 L860 480 L0 480 Z" fill="#9bcb3c"/>
    <path d="M0 0 C120 70 300 130 560 150 C680 160 780 150 860 135 L860 150 C760 168 660 176 540 168 C300 150 120 95 0 25 Z" fill="#3a3a3a"/>
    <path d="M0 25 C120 95 300 150 540 168 C660 176 760 168 860 150 L860 165 C760 185 640 192 520 186 C300 170 120 120 0 55 Z" fill="#add136"/>
    <path d="M0 55 C120 120 300 170 520 186 C640 192 760 185 860 165 L860 200 C600 230 300 210 0 130 Z" fill="#cadf82"/>
  </svg>

  <div class="badge" role="img" aria-label="Accreditation badge"></div>

  <section class="services">
    <h2>OUR<br>SERVICES</h2>
    <ul>
      <li>Free Loft and Cavity Insulation</li>
      <li>Energy Reduction</li>
      <li>Carbon Emission Reduction</li>
      <li>Energy Saving Tips</li>
      <li>Making Homes Warmer</li>
    </ul>
  </section>

  <section class="contact">
    <p class="phone">CONTACT: 08000 614 905</p>
    <p class="email">Email: epc@th-tidewell.co.uk</p>
  </section>

  <div class="consult">Consultations<br>in the comfort<br>of your own<br>home</div>

  <section class="territory">
    <h3>Nationwide (UK)</h3>
    <p>Harrowfield Business Centre, Kestrel<br>Road, Perth, PH2 7QL.</p>
  </section>
</main>
</body>
</html>
```